Retro Cartoon Tattoo Flash Event Ad Creative

I am seeking a vibrant and eye-catching ad creative for my upcoming tattoo flash event, themed around retro cartoons.
My event will feature tattoo designs inspired by popular retro cartoons like Pebblefin, Zoomstar Kids, and other nostalgic characters.
Objectives:
The ad should attract a diverse audience, appealing especially to fans of 90s and early 2000s cartoons.
It must be visually engaging, incorporating elements that evoke a sense of nostalgia and fun.
Design Requirements:
Size: 1080 x 1080 px
Visual Style: The design should be colorful, dynamic, and playful.
Text Content: Include the event name "Retro Cartoon Tattoo Flash Event", the dates, location, and a call-to-action "Book Your Spot Now!".
Dates: May 13 - 31
Location: Nine Lantern Tattoos in Woodruff, SC
I have uploaded several images that you may use in the creative if you'd like. This includes an image of the tattoo artist, her logo, and the tattoo designs for the event.

```html
<!DOCTYPE html>
<html lang="en">
<head>
<meta charset="utf-8">
<title>Retro Cartoon Tattoo Flash Event</title>
<link rel="stylesheet" href="https://fonts.googleapis.com/css2?family=IM+Fell+English+SC&family=Luckiest+Guy&family=Bowlby+One&display=swap">
<style>
  :root {
    --ink: #000000;
    --paper: #ffffff;
    --art-tone: #d9d9d9;
    --art-tone-dark: #8c8c8c;
  }
  * { margin: 0; padding: 0; box-sizing: border-box; }
  html, body { width: 720px; height: 1200px; overflow: hidden; background: var(--paper); }
  .poster { position: relative; width: 720px; height: 1200px; background: var(--paper); color: var(--ink); overflow: hidden; }
  .art { position: absolute; background: var(--art-tone); border-radius: 8px; }
  .art--dark { background: var(--art-tone-dark); }
  .layer { position: absolute; left: 0; top: 0; width: 720px; height: 1200px; overflow: hidden; }
  .layer text { white-space: pre; }
  .serif { font-family: "IM Fell English SC", serif; fill: var(--ink); }
  .outline-title {
    font-family: "Luckiest Guy", sans-serif; fill: var(--paper); stroke: var(--ink);
    stroke-width: 4; paint-order: stroke fill;
  }
  .flash-event { font-family: "Bowlby One", sans-serif; fill: var(--ink); }
  .cta-band { fill: var(--ink); }
  .cta-text { font-family: "Luckiest Guy", sans-serif; fill: var(--paper); }
  .frame-line { fill: none; stroke: var(--ink); stroke-width: 5; stroke-linecap: square; }
  .rule { stroke: var(--ink); stroke-width: 3; }
</style>
</head>
<body>
<main class="poster">

  <div class="art" style="left:153px; top:104px; width:89px; height:50px;" role="img" aria-label="Tattoo flash flower with leaves ornament"></div>
  <div class="art" style="left:482px; top:104px; width:89px; height:50px;" role="img" aria-label="Tattoo flash flower with leaves ornament"></div>
  <div class="art" style="left:68px; top:279px; width:134px; height:94px;" role="img" aria-label="Old-school shark leaping from waves illustration"></div>
  <div class="art" style="left:560px; top:276px; width:124px; height:100px;" role="img" aria-label="Old-school swallow bird illustration"></div>
  <div class="art" style="left:196px; top:502px; width:340px; height:300px;" role="img" aria-label="Line illustration of a hairless cat wearing glasses, event flash design"></div>
  <div class="art art--dark" style="left:73px; top:917px; width:99px; height:87px;" role="img" aria-label="Heart pierced by an arrow ornament"></div>
  <div class="art art--dark" style="left:580px; top:917px; width:104px; height:87px;" role="img" aria-label="Heart pierced by an arrow ornament"></div>

  <svg class="layer" viewBox="0 0 720 1200">
    <g aria-hidden="true">
      <path class="frame-line" d="M160 417 H106 V853 H243"/>
      <path class="frame-line" d="M102 423 V847"/>
      <path class="frame-line" d="M570 417 H621 V853 H492"/>
      <path class="frame-line" d="M623 428 H633 V848"/>
    </g>

    <text class="serif" x="360" y="146" text-anchor="middle" font-size="54" textLength="200" lengthAdjust="spacingAndGlyphs">RETRO</text>
    <text class="outline-title" x="349" y="264" text-anchor="middle" font-size="112" textLength="414" lengthAdjust="spacingAndGlyphs">CARTOON</text>
    <text class="outline-title" x="373" y="370" text-anchor="middle" font-size="104" textLength="350" lengthAdjust="spacingAndGlyphs">TATTOO</text>
    <text class="flash-event" x="361" y="450" text-anchor="middle" font-size="60" textLength="360" lengthAdjust="spacingAndGlyphs">FLASH EVENT</text>

    <text class="serif" x="369" y="867" text-anchor="middle" font-size="36" textLength="205" lengthAdjust="spacingAndGlyphs">WHISKER INK</text>

    <text class="serif" x="372" y="962" text-anchor="middle" font-size="66" textLength="366" lengthAdjust="spacingAndGlyphs">MAY 13 - 31</text>

    <line class="rule" x1="186" y1="1005" x2="252" y2="1005"/>
    <text class="serif" x="369" y="1016" text-anchor="middle" font-size="30" textLength="222" lengthAdjust="spacingAndGlyphs">{ LOCATION }</text>
    <line class="rule" x1="488" y1="1005" x2="562" y2="1005"/>
    <text class="serif" x="371" y="1051" text-anchor="middle" font-size="25" textLength="574" lengthAdjust="spacingAndGlyphs">NINE LANTERN TATTOOS IN WOODRUFF, SC</text>

    <rect class="cta-band" x="0" y="1074" width="720" height="126"/>
    <text class="cta-text" x="87" y="1158" font-size="52" textLength="173" lengthAdjust="spacingAndGlyphs">BOOK</text>
    <text class="cta-text" x="281" y="1152" font-size="30" textLength="192" lengthAdjust="spacingAndGlyphs">YOUR SPOT</text>
    <text class="cta-text" x="495" y="1158" font-size="52" textLength="165" lengthAdjust="spacingAndGlyphs">NOW!</text>
  </svg>

</main>
</body>
</html>
```